Paws Home

Need Yard signs
Dimensions 24" wide and 18" high

Copy: Rescue does not mean "Damaged". It means they have been let down by humans.
Please adopt at: 217 W Brannock Ave, Tampa, Fl 33682
Open: Tues-Sun 10am - 7pm

I have attached a sample of the original ad. I can't use this because the resolution is too low and the type has to be big enough so that it can be seen 12 feet away.
I have also attached some photos you can use. The res may not be hi enough, but perhaps you can find some stock photography even these pics are not hi res enough.

Target Market(s)

animal lovers

Font styles to use
Sans Serif

Colors

Designer to choose colors to be used in the design.

Requirements
Must have
• Must be easy to read.

```html
<!DOCTYPE html>
<html lang="en">
<head>
<meta charset="utf-8">
<title>Paws Home – Yard Sign</title>
<link href="https://fonts.googleapis.com/css2?family=Montserrat:wght@600;800&display=swap" rel="stylesheet">
<style>
  :root {
    --navy: #0b1063;
    --green: #8cc63f;
    --grey: #555a5f;
    --paper: #ffffff;
    --backdrop: #e6e7ea;
    --photo-light: #d9cbb4;
    --photo-mid: #b58a55;
    --photo-dark: #7b8e94;
  }
  * { margin: 0; padding: 0; box-sizing: border-box; }
  html, body { width: 960px; height: 1200px; overflow: hidden; background: var(--backdrop); }
  body { position: relative; font-family: "Montserrat", sans-serif; }

  /* 24" x 18" landscape yard sign, scaled to 960 x 720 */
  .sign {
    position: absolute;
    left: 0;
    top: 240px;
    width: 960px;
    height: 720px;
    background: var(--paper);
    overflow: hidden;
  }
  .hero-photo {
    position: absolute;
    left: 16px;
    top: 12px;
    width: 460px;
    height: 548px;
  }
  .brand {
    position: absolute;
    left: 490px;
    top: 48px;
    width: 440px;
    display: flex;
    align-items: center;
    justify-content: center;
    gap: 14px;
    color: var(--navy);
    font-weight: 800;
    font-size: 44px;
    line-height: 54px;
    white-space: nowrap;
  }
  .brand-dot {
    width: 22px;
    height: 22px;
    border-radius: 50%;
    background: var(--green);
    flex: none;
  }
  .message-frame {
    position: absolute;
    left: 490px;
    top: 190px;
    width: 440px;
    height: 300px;
    border: 1.5px solid var(--navy);
    box-shadow: 0 22px 20px -16px rgba(0,0,0,0.18);
    text-align: center;
  }
  .message-lead {
    position: absolute;
    top: -20px;
    left: 50%;
    transform: translateX(-50%);
    padding: 0 12px;
    background: var(--paper);
    color: var(--grey);
    font-weight: 600;
    font-size: 29px;
    line-height: 38px;
    white-space: nowrap;
  }
  .message-key {
    margin-top: 46px;
    color: var(--green);
    font-weight: 800;
    font-size: 74px;
    line-height: 84px;
    letter-spacing: -1px;
  }
  .message-tail {
    margin-top: 16px;
    color: var(--grey);
    font-weight: 600;
    font-size: 27px;
    line-height: 38px;
    white-space: nowrap;
  }
  .info-band {
    position: absolute;
    left: 0;
    bottom: 0;
    width: 960px;
    height: 150px;
    background: var(--navy);
    color: var(--paper);
    display: flex;
    flex-direction: column;
    align-items: center;
    justify-content: center;
    gap: 8px;
  }
  .info-row {
    display: flex;
    align-items: center;
    gap: 16px;
    font-weight: 600;
    font-size: 42px;
    line-height: 52px;
    white-space: nowrap;
  }
  .info-row.address { font-size: 38px; }
  .info-icon { flex: none; }
</style>
</head>
<body>
<main class="sign">
  <svg class="hero-photo" viewBox="0 0 460 548" role="img" aria-label="Photo of a tan and white rescue dog sitting in a shelter kennel, looking up sadly">
    <defs>
      <linearGradient id="photoTone" x1="0" y1="0" x2="1" y2="0.3">
        <stop offset="0" stop-color="var(--photo-dark)"/>
        <stop offset="0.35" stop-color="var(--photo-light)"/>
        <stop offset="0.6" stop-color="var(--photo-mid)"/>
        <stop offset="1" stop-color="var(--photo-light)"/>
      </linearGradient>
    </defs>
    <path fill="url(#photoTone)" d="M120 8 L360 0 L372 30 L345 52 L390 70 L415 110 L432 160 L452 215 L438 245 L458 285 L440 320 L460 370 L446 415 L440 470 L430 535 L398 518 L362 548 L318 520 L262 542 L206 522 L150 546 L100 520 L60 538 L42 505 L50 460 L24 438 L28 385 L6 350 L0 310 L12 270 L2 235 L30 205 L18 170 L60 150 L82 112 L118 92 L132 56 L108 32 Z"/>
  </svg>

  <div class="brand"><span class="brand-dot"></span><span>Paws Home</span></div>

  <section class="message-frame">
    <p class="message-lead">RESCUE DOES NOT MEAN</p>
    <h1 class="message-key">DAMAGED</h1>
    <p class="message-tail">IT MEANS THEY HAVE BEEN<br>LET DOWN BY HUMANS</p>
  </section>

  <footer class="info-band">
    <div class="info-row hours">
      <svg class="info-icon" width="36" height="36" viewBox="0 0 36 36" aria-hidden="true">
        <rect x="2" y="6" width="26" height="24" rx="2" fill="none" stroke="var(--green)" stroke-width="2.5"/>
        <rect x="2" y="6" width="26" height="6" fill="var(--green)"/>
        <rect x="8" y="2" width="3" height="7" fill="var(--green)"/>
        <rect x="19" y="2" width="3" height="7" fill="var(--green)"/>
        <g fill="var(--green)">
          <rect x="6" y="15" width="4" height="3"/><rect x="12" y="15" width="4" height="3"/><rect x="18" y="15" width="4" height="3"/>
          <rect x="6" y="21" width="4" height="3"/><rect x="12" y="21" width="4" height="3"/>
        </g>
        <circle cx="27" cy="27" r="7.5" fill="var(--navy)" stroke="var(--green)" stroke-width="2.5"/>
        <path d="M27 23 V27.5 H30" fill="none" stroke="var(--green)" stroke-width="2"/>
      </svg>
      <span>Tues-Sun 10am - 7pm</span>
    </div>
    <div class="info-row address">
      <svg class="info-icon" width="26" height="36" viewBox="0 0 26 36" aria-hidden="true">
        <path d="M13 1 C6 1 1 6.5 1 13 C1 22 13 35 13 35 C13 35 25 22 25 13 C25 6.5 20 1 13 1 Z" fill="var(--green)"/>
        <circle cx="13" cy="13" r="4.5" fill="var(--navy)"/>
      </svg>
      <span>217 W Brannock Ave, Tampa, Fl 33682</span>
    </div>
  </footer>
</main>
</body>
</html>
```